beauty salon

providing waxing services from a home base this must include which I will provide a price list and an address

Industry/Entity Type

Beauty Salon

Font styles to use
Script

Colors

Designer to choose colors to be used in the design.

```html
<!DOCTYPE html>
<html lang="en">
<head>
<meta charset="utf-8">
<title>Marlee's Place Salon – Price List</title>
<link rel="stylesheet" href="https://fonts.googleapis.com/css2?family=Dancing+Script:wght@500;600&family=Open+Sans:wght@400;700&family=Arimo:wght@400;700&display=swap">
<style>
  :root {
    --paper: #ffffff;
    --title: #b867b3;
    --hot-pink: #e8198b;
    --ink: #111111;
    --band: #f2a6c8;
    --band-deep: #e985b3;
  }
  * { margin: 0; padding: 0; box-sizing: border-box; }
  html, body { width: 1200px; height: 851px; overflow: hidden; background: var(--paper); }
  .flyer { position: relative; width: 1200px; height: 851px; overflow: hidden; background: var(--paper); font-family: "Open Sans", sans-serif; color: var(--ink); }
  .backdrop { position: absolute; inset: 0; }

  .tagline, .salon-name { position: absolute; left: 0; width: 1236px; text-align: center; font-family: "Dancing Script", cursive; color: var(--title); white-space: nowrap; }
  .tagline { top: 22px; font-size: 52px; font-weight: 500; letter-spacing: 1px; }
  .salon-name { top: 70px; font-size: 86px; font-weight: 600; letter-spacing: 1px; line-height: 1.1; }
  .qualification { position: absolute; top: 164px; left: 0; width: 1260px; text-align: center; font-family: "Arimo", sans-serif; font-weight: 700; font-size: 18px; color: var(--hot-pink); }
  .mobile { position: absolute; top: 204px; left: 936px; font-family: "Arimo", sans-serif; font-weight: 700; font-size: 18px; }
  .mobile span { color: var(--hot-pink); }

  .symbol-spot { position: absolute; left: 122px; top: 70px; width: 84px; height: 84px; border-radius: 50%; background: radial-gradient(circle, #f4a6a0 0%, #9fc3ee 70%, rgba(255,255,255,0) 100%); }

  .offer { position: absolute; left: 960px; top: 18px; width: 190px; height: 122px; }
  .offer-text { position: absolute; left: 990px; top: 40px; width: 150px; text-align: center; color: #fff; font-family: "Arimo", sans-serif; font-size: 15px; line-height: 18px; }

  .price-list { position: absolute; }
  .price-list h2 { font-size: 21px; font-weight: 700; line-height: 28.8px; }
  .price-list li { list-style: none; display: flex; font-size: 21px; line-height: 28.8px; }
  .price-list .item { flex: 0 0 var(--name-w); }
  .ladies { left: 142px; top: 238px; --name-w: 286px; }
  .eyes { left: 731px; top: 247px; --name-w: 284px; }
  .mens { left: 736px; top: 441px; --name-w: 285px; }

  .hours { position: absolute; left: 514px; top: 390px; font-family: "Arimo", sans-serif; font-weight: 700; font-size: 18px; line-height: 23px; }
  .hours h3 { font-size: 18px; text-align: center; padding-left: 36px; }
  .hours p { color: var(--hot-pink); white-space: pre; }

  .address { position: absolute; top: 788px; left: 0; width: 1204px; text-align: center; font-family: "Arimo", sans-serif; font-weight: 700; font-size: 19px; }
  .address span { color: var(--hot-pink); }
</style>
</head>
<body>
<main class="flyer">
  <svg class="backdrop" viewBox="0 0 1200 851" width="1200" height="851">
    <defs>
      <radialGradient id="petals" cx="50%" cy="50%" r="50%">
        <stop offset="0" stop-color="#f4b3d1"/>
        <stop offset="0.6" stop-color="#fad7e7"/>
        <stop offset="1" stop-color="#ffffff" stop-opacity="0"/>
      </radialGradient>
      <linearGradient id="cloudFill" x1="0" y1="0" x2="1" y2="1">
        <stop offset="0" stop-color="#f9b3d3"/>
        <stop offset="1" stop-color="#e0529b"/>
      </linearGradient>
    </defs>
    <g role="img" aria-label="Soft pink blossom decoration">
      <ellipse cx="90" cy="90" rx="200" ry="170" fill="url(#petals)"/>
      <ellipse cx="260" cy="40" rx="110" ry="60" fill="url(#petals)"/>
      <ellipse cx="1120" cy="200" rx="150" ry="230" fill="url(#petals)" opacity="0.6"/>
      <ellipse cx="60" cy="660" rx="110" ry="100" fill="url(#petals)" opacity="0.6"/>
      <ellipse cx="1130" cy="700" rx="140" ry="140" fill="url(#petals)"/>
      <ellipse cx="640" cy="650" rx="110" ry="100" fill="url(#petals)" opacity="0.7"/>
      <ellipse cx="960" cy="750" rx="120" ry="80" fill="url(#petals)" opacity="0.7"/>
    </g>
    <path d="M0 600 C 220 560 420 560 620 620 S 960 760 1200 730 L 1200 770 C 960 800 780 730 600 660 S 220 600 0 640 Z" fill="var(--band)" opacity="0.3"/>
    <path d="M0 625 C 240 590 430 600 640 670 S 980 800 1200 790 L 1200 812 C 980 830 760 760 620 700 S 220 640 0 655 Z" fill="var(--band-deep)" opacity="0.25"/>
    <path d="M0 660 C 260 620 460 650 660 720 S 1000 840 1200 830" fill="none" stroke="var(--band)" stroke-width="2" opacity="0.5"/>
  </svg>

  <div class="symbol-spot" role="img" aria-label="Small male and female symbol icon"></div>

  <svg class="offer" viewBox="0 0 190 122" width="190" height="122" aria-hidden="true">
    <path d="M40 18 C 60 0 100 0 118 14 C 140 2 178 10 180 40 C 192 60 184 92 160 98 C 140 116 100 112 84 104 C 60 114 20 106 22 84 C 0 72 6 36 40 18 Z" fill="url(#cloudFill)"/>
    <circle cx="18" cy="112" r="7" fill="#f4b3d1"/>
  </svg>
  <p class="offer-text">10%<br>Discount<br>on First Treatment</p>

  <p class="tagline">Beauty Therapist</p>
  <h1 class="salon-name">Marlee's Place Salon</h1>
  <p class="qualification">Diploma of Beauty Therapy at Avery Lane</p>
  <p class="mobile">Mobile: <span>0400 118 275</span></p>

  <section class="price-list ladies">
    <h2>Lady's Waxing</h2>
    <ul>
      <li><span class="item">Eyebrow</span><span>$8</span></li>
      <li><span class="item">Upper lip</span><span>$8</span></li>
      <li><span class="item">Chin</span><span>$8</span></li>
      <li><span class="item">Face wax</span><span>$25</span></li>
      <li><span class="item">Bikini line</span><span>$15</span></li>
      <li><span class="item">G string</span><span>$20</span></li>
      <li><span class="item">½ Brazilian</span><span>$30</span></li>
      <li><span class="item">Full Brazilian</span><span>$40</span></li>
      <li><span class="item">Half arm</span><span>$20</span></li>
      <li><span class="item">Upper half arm</span><span>$20</span></li>
      <li><span class="item">Full arm</span><span>$25</span></li>
      <li><span class="item">Half leg</span><span>$15</span></li>
      <li><span class="item">Upper leg</span><span>$20</span></li>
      <li><span class="item">¾ Leg</span><span>$25</span></li>
      <li><span class="item">Full leg</span><span>$35</span></li>
    </ul>
  </section>

  <section class="price-list eyes">
    <h2>Eye Enhancement</h2>
    <ul>
      <li><span class="item">Eyebrow tint</span><span>$12</span></li>
      <li><span class="item">Eyelash tint</span><span>$15</span></li>
    </ul>
  </section>

  <section class="hours">
    <h3>Now open:</h3>
    <p>Wed    10am - 4pm</p>
    <p> Frid    10am - 7pm</p>
    <p>  Sat   10am - 4pm</p>
  </section>

  <section class="price-list mens">
    <h2>Men's Waxing</h2>
    <ul>
      <li><span class="item">Eyebrow</span><span>$10</span></li>
      <li><span class="item">Half arm</span><span>$20</span></li>
      <li><span class="item">Upper half arm</span><span>$25</span></li>
      <li><span class="item">Full arm</span><span>$30</span></li>
      <li><span class="item">Half leg</span><span>$25</span></li>
      <li><span class="item">Full leg</span><span>$45</span></li>
      <li><span class="item">Chest wax</span><span>$40</span></li>
      <li><span class="item">Back wax</span><span>$35</span></li>
    </ul>
  </section>

  <p class="address">Address: <span>12 Finch Lane Oakridge Park</span></p>
</main>
</body>
</html>
```